Lorvel Tiered Food/Dessert Trays Spec Sheet

We need an elegant spec sheet template to use with our food/dessert trays. This will accompany the item when it ships out and on the web. It is something we would like to email our customers when they are considering our different banquet trays. It is important that it does not look too retail. We are the manufacturer and do not sell retail. We are business to business. It needs to help a salesman make a sale and look elegant enough while conveying the info to them.
Updates

Target Market(s)

Banquet Halls, Caterers, Country Clubs, Wedding and event centers.

Industry/Entity Type

Event

Font styles to use
Serif
Decorative
Script

Requirements
Must have
• All the copy in the word doc. Also use the model name as the heading at the top of the sheet
Nice to have
• An elegant but professional look
Should not have
• Not too busy

```html
<!DOCTYPE html>
<html lang="en">
<head>
<meta charset="utf-8">
<title>Crown Deluxe – Three-Tier Buffet Stand</title>
<link rel="stylesheet" href="https://fonts.googleapis.com/css2?family=Playfair+Display:wght@400;700&family=Lora:wght@400;700&family=Pinyon+Script&display=swap">
<style>
  :root {
    --navy: #2d2a88;
    --gold: #9a8a5c;
    --gold-seal: #c9b777;
    --ink: #2a2a2a;
    --paper-top: #f4f4f4;
    --paper-top-edge: #e9e9e9;
    --linen: #efefef;
    --panel: #fbfbfb;
    --line: #d7d2c2;
  }
  * { margin: 0; padding: 0; box-sizing: border-box; }
  html, body { width: 900px; height: 1200px; overflow: hidden; }
  body { font-family: "Lora", Georgia, serif; color: var(--ink); background: var(--linen); }
  .sheet { position: relative; width: 900px; height: 1200px; overflow: hidden; }
  .upper-band {
    position: absolute; left: 0; top: 0; width: 900px; height: 536px;
    background: radial-gradient(ellipse at 60% 40%, #fafafa 0%, var(--paper-top) 55%, var(--paper-top-edge) 100%);
  }
  .lower-band {
    position: absolute; left: 0; top: 536px; width: 900px; height: 664px;
    background: linear-gradient(180deg, #ececec 0%, var(--linen) 40%, #f2f2f2 100%);
  }
  .model-name {
    position: absolute; left: 66px; top: 48px;
    font-family: "Playfair Display", Georgia, serif; font-weight: 400;
    font-size: 92px; line-height: 1; color: var(--navy);
  }
  .product-type {
    position: absolute; left: 546px; top: 180px; width: 320px;
    font-family: "Playfair Display", Georgia, serif; font-weight: 400;
    font-size: 52px; line-height: 1.05; color: var(--navy);
    padding-bottom: 8px; border-bottom: 2px solid var(--navy);
  }
  .intro {
    position: absolute; left: 548px; top: 318px; width: 320px;
    font-size: 17px; line-height: 1.38; color: var(--ink);
  }
  .intro p { margin-bottom: 16px; }
  .product-photo {
    position: absolute; left: 48px; top: 178px; width: 530px; height: 562px;
    border-radius: 8px;
    background: radial-gradient(ellipse at 50% 55%, #e4e0cf 0%, #cfc9b0 40%, rgba(220,216,200,0.35) 75%, rgba(240,240,240,0) 100%);
  }
  .tagline {
    position: absolute; left: 588px; top: 634px;
    font-family: "Pinyon Script", cursive; font-size: 40px; line-height: 1.25; color: var(--gold);
  }
  .tagline span { display: block; }
  .tagline span + span { padding-left: 54px; }
  .details {
    position: absolute; left: 62px; top: 782px; width: 782px; height: 268px;
    background: var(--panel); border: 1px solid var(--line); border-radius: 8px;
    display: grid; grid-template-columns: 360px 1fr; overflow: hidden;
    box-shadow: 0 1px 3px rgba(0,0,0,0.08);
  }
  .details-col + .details-col { border-left: 1px solid var(--line); }
  .details-col h2 {
    background: var(--gold); color: #fff; text-align: center;
    font-family: "Lora", Georgia, serif; font-weight: 700; font-size: 18px;
    height: 38px; line-height: 38px;
  }
  .details-col ul { list-style: none; padding: 14px 0 0 26px; }
  .details-col li { position: relative; padding-left: 16px; font-size: 15px; line-height: 1.2; }
  .details-col li::before {
    content: ""; position: absolute; left: 0; top: 7px; width: 5px; height: 5px;
    border-radius: 50%; background: var(--gold);
  }
  .spec-list li { margin-bottom: 14px; }
  .feature-list li { margin-bottom: 9px; }
  .brand {
    position: absolute; left: 62px; top: 1092px; height: 64px;
    display: flex; align-items: center;
  }
  .brand-mark { width: 30px; height: 30px; border-radius: 50%; background: var(--navy); margin-right: 12px; }
  .brand-name {
    font-family: "Lora", Georgia, serif; font-weight: 400; font-size: 28px; line-height: 1;
    color: var(--navy);
    padding-right: 18px; border-right: 1px solid var(--navy); margin-right: 14px;
    height: 44px; display: flex; align-items: center;
  }
  .contact-phone { font-size: 17px; font-weight: 700; color: var(--navy); line-height: 1.2; }
  .contact-fax { font-size: 13px; color: var(--navy); }
  .contact-web { margin-left: 18px; font-size: 14px; color: var(--navy); line-height: 1.4; }
  .warranty-seal {
    position: absolute; left: 684px; top: 1054px; width: 118px; height: 118px;
    border-radius: 50%;
    background: radial-gradient(circle at 40% 35%, #e3d59c 0%, var(--gold-seal) 55%, #a89655 100%);
    box-shadow: 0 0 0 4px #d8ca8e, 0 2px 4px rgba(0,0,0,0.2);
    display: flex; flex-direction: column; align-items: center; justify-content: center;
    font-family: "Lora", Georgia, serif; color: #4a3f1c; text-align: center; line-height: 1.05;
  }
  .warranty-seal .years { font-family: "Playfair Display", Georgia, serif; font-size: 26px; }
  .warranty-seal .terms { font-size: 14px; }
</style>
</head>
<body>
<main class="sheet">
  <div class="upper-band"></div>
  <div class="lower-band"></div>

  <h1 class="model-name">Crown Deluxe</h1>
  <div class="product-photo" role="img" aria-label="Photo of the polished silver three-tier buffet stand with three round trays on a central column and pedestal base"></div>

  <h2 class="product-type">Three-Tier Buffet Stand</h2>
  <div class="intro">
    <p>This eye catching stand with its large tray sizes make it an excellent choice for serving large groups at banquets, buffets or any catering operation.</p>
    <p>Create stunning appetizers, finger foods, main courses and more.</p>
    <p>This stand is a true caterers dream...</p>
  </div>

  <p class="tagline"><span>No tarnish.</span><span>No polish.</span></p>

  <section class="details">
    <div class="details-col">
      <h2>Specifications</h2>
      <ul class="spec-list">
        <li>Code: CRNIII24-1814-S</li>
        <li>Height: 33"</li>
        <li>Trays sizes: 14", 24", 18"</li>
        <li>Total weight: 20 lbs</li>
        <li>Shipping weight: 28 lbs</li>
        <li>Shipping dimensions: 27"x 27"x 10"</li>
      </ul>
    </div>
    <div class="details-col">
      <h2>Features</h2>
      <ul class="feature-list">
        <li>Designed for repeated commercial use</li>
        <li>High polished stainless steel trays &amp; base</li>
        <li>Decorative silver bow tie trim on the base</li>
        <li>Nickel plated silver columns</li>
        <li>Self-serving buffet station</li>
        <li>No tools needed for assembly or disassembly</li>
        <li>Breaks down for easy clean up and storage</li>
      </ul>
    </div>
  </section>

  <footer class="brand">
    <span class="brand-mark"></span>
    <span class="brand-name">Lorvel</span>
    <div class="contact-phones">
      <div class="contact-phone">800-555-0142</div>
      <div class="contact-fax">Fax: 215-555-0198</div>
    </div>
    <div class="contact-web">
      <div>www.lorvel.com</div>
      <div>info@lorvel.com</div>
    </div>
  </footer>

  <div class="warranty-seal">
    <span class="years">1 year</span>
    <span class="terms">limited</span>
    <span class="terms">warranty</span>
  </div>
</main>
</body>
</html>
```